LedgerNook Project
LedgerNook
Project: LedgerNook Project
LedgerNook Project - Financial Services
Creative Brief
Bright & Fun-filled
Peter Halvik
President
Leave blank
peter@ledgernook.example
www.ledgernook.example
The front should be white with logo, my name, cell phone, email address, and website. Leave address blank because there is no physical address at the moment. List these services with bullet point. (accounting, bookkeeping, and payroll) Please make sure the design meet GlossPrint silk laminate with spot uv because I plan to use them to print in the future. Check link: http://www.glossprint.example/Business-Cards/Silk-Business-Cards-with-Spot-UV-and-Rounded-Corners
I want the back to be a solid color with logo. Check link for what I am looking for: http://www.glossprint.example/Inspiration-Gallery#/gallery/img/images_M.jpg

```html
<!DOCTYPE html>
<html lang="en">
<head>
<meta charset="utf-8">
<title>LedgerNook Business Card</title>
<link rel="stylesheet" href="https://fonts.googleapis.com/css2?family=PT+Sans:wght@400;700&display=swap">
<style>
  :root {
    --backdrop: #ebe8e3;
    --card: #ffffff;
    --brand-blue: #3d8fd4;
    --brand-navy: #1c3a5e;
    --ink: #1e1e1e;
    --rule: #b9c6d3;
    --on-blue: #ffffff;
  }
  * { margin: 0; padding: 0; box-sizing: border-box; }
  html, body { width: 1200px; height: 751px; overflow: hidden; }
  body {
    background: var(--backdrop);
    font-family: "PT Sans", Arial, sans-serif;
    color: var(--ink);
    position: relative;
  }
  .card {
    position: absolute;
    top: 225px;
    width: 540px;
    height: 300px;
    background: var(--card);
    border-radius: 26px;
    overflow: hidden;
    box-shadow: 0 4px 14px rgba(0,0,0,.12);
  }
  .card--front { left: 40px; }
  .card--back { left: 620px; background: var(--brand-blue); }

  .brand {
    position: absolute;
    display: flex;
    flex-direction: column;
    align-items: center;
  }
  .brand__mark {
    width: 64px;
    height: 64px;
    background: var(--brand-blue);
    border-radius: 6px;
    margin-bottom: 10px;
  }
  .brand__name {
    font-weight: 700;
    font-size: 36px;
    color: var(--brand-navy);
    letter-spacing: -0.5px;
    line-height: 1;
  }
  .card--front .brand { left: 20px; top: 44px; width: 220px; }

  .divider {
    position: absolute;
    left: 252px;
    top: 32px;
    width: 1px;
    height: 150px;
    background: var(--rule);
  }
  .contact {
    position: absolute;
    left: 272px;
    top: 36px;
    font-size: 15px;
    line-height: 1.35;
  }
  .contact__name {
    font-weight: 700;
    font-size: 22px;
    line-height: 1.1;
  }
  .contact__title { font-size: 17px; margin-bottom: 30px; }
  .contact__label { font-weight: 700; }

  .band {
    position: absolute;
    left: 0;
    right: 0;
    top: 222px;
    height: 22px;
    background: var(--brand-blue);
    border-top: 3px solid var(--brand-navy);
  }
  .services {
    position: absolute;
    left: 0;
    right: 0;
    top: 256px;
    display: flex;
    justify-content: center;
    gap: 34px;
    list-style: none;
    font-size: 14px;
    color: var(--brand-navy);
  }
  .services__item::before {
    content: "";
    display: inline-block;
    width: 7px;
    height: 7px;
    border-radius: 50%;
    background: var(--brand-blue);
    margin-right: 8px;
    vertical-align: 2px;
  }

  .card--back .brand { left: 0; right: 0; top: 64px; }
  .card--back .brand__mark { width: 80px; height: 80px; background: var(--on-blue); }
  .card--back .brand__name { font-size: 44px; color: var(--on-blue); }
  .back__web {
    position: absolute;
    left: 0; right: 0;
    bottom: 36px;
    text-align: center;
    font-size: 14px;
    color: var(--on-blue);
  }
</style>
</head>
<body>
  <section class="card card--front">
    <div class="brand">
      <div class="brand__mark"></div>
      <div class="brand__name">LedgerNook</div>
    </div>
    <div class="divider"></div>
    <div class="contact">
      <div class="contact__name">Peter Halvik</div>
      <div class="contact__title">President</div>
      <div>Leave blank</div>
      <div><span class="contact__label">Cell:</span> 334-555-0182</div>
      <div><span class="contact__label">Email:</span> peter@ledgernook.example</div>
      <div>www.ledgernook.example</div>
    </div>
    <div class="band"></div>
    <ul class="services">
      <li class="services__item">Accounting</li>
      <li class="services__item">Bookkeeping</li>
      <li class="services__item">Payroll</li>
    </ul>
  </section>

  <section class="card card--back">
    <div class="brand">
      <div class="brand__mark"></div>
      <div class="brand__name">LedgerNook</div>
    </div>
    <div class="back__web">www.ledgernook.example</div>
  </section>
</body>
</html>
```